Merrow Sailcraft Works President Business Card Carbon fiber catamarans

Hi.. I need a new business card design.. I am the President of a high tech yacht builder. We build Carbon Fiber go fast catamarans... Maybe we use the file I am sharing to you as the back of the card.. We need to look cool and crisp ...

Target Market(s)

Affluent People who will purchase a cool yacht

Industry/Entity Type

Custom Yacht Builder

Contact Information for Business Card

Dale Penwarty , President, 517.608.2391 USA

Font styles to use
Serif

Requirements
Must have
• the clean crisp cool feel
Nice to have
• clean and crisp
Should not have
• Bold ugly

```html
<!DOCTYPE html>
<html lang="en">
<head>
<meta charset="utf-8">
<title>Merrow Sailcraft Works – Business Card</title>
<link rel="stylesheet" href="https://fonts.googleapis.com/css2?family=Roboto:wght@400;700&display=swap">
<style>
  :root {
    --backdrop: #141414;
    --card: #2b2b2d;
    --card-edge: #4a4a4d;
    --silver: #d4d5d8;
    --silver-dim: #a9abb0;
    --rule: #8d8f94;
  }
  * { margin: 0; padding: 0; box-sizing: border-box; }
  html, body {
    width: 1200px; height: 963px; overflow: hidden;
    background: var(--backdrop);
    font-family: "Roboto", Arial, sans-serif;
  }
  .canvas { position: relative; width: 1200px; height: 963px; }
  .card {
    position: absolute;
    width: 620px; height: 354px;
    background: var(--card);
    border: 1px solid var(--card-edge);
    border-radius: 22px;
    box-shadow: 0 18px 40px rgba(0,0,0,.6);
    color: var(--silver);
  }
  .card--front { left: 70px; top: 100px; }
  .card--back { left: 510px; top: 510px; }

  .brand { display: flex; align-items: center; gap: 12px; }
  .brand__mark { width: 30px; height: 30px; border: 2px solid var(--silver); border-radius: 50%; }
  .brand__name {
    font-size: 26px; font-weight: 400; letter-spacing: 3px;
    text-transform: uppercase; color: var(--silver); line-height: 1.1;
  }
  .card--front .brand { position: absolute; right: 40px; top: 88px; }
  .card--back .brand { position: absolute; left: 50%; top: 50%; transform: translate(-50%, -50%); }
  .card--back .brand__name { font-size: 30px; }

  .contact { position: absolute; left: 38px; top: 118px; }
  .contact__name { font-size: 19px; font-weight: 700; letter-spacing: .5px; text-transform: uppercase; }
  .contact__role { font-size: 14px; color: var(--silver-dim); margin-top: 2px; }
  .contact__list { list-style: none; margin-top: 18px; }
  .contact__item { display: flex; align-items: center; gap: 8px; font-size: 15px; line-height: 24px; }
  .contact__item svg { width: 13px; height: 13px; fill: var(--silver-dim); }

  .rule { position: absolute; left: 38px; right: 40px; top: 172px; height: 1px; background: var(--rule); }
  .address { position: absolute; right: 40px; bottom: 34px; text-align: right; font-size: 15px; line-height: 20px; color: var(--silver); }
</style>
</head>
<body>
<main class="canvas">
  <section class="card card--front" aria-label="Card front">
    <div class="brand">
      <span class="brand__mark"></span>
      <span class="brand__name">Merrow Sailcraft Works</span>
    </div>
    <div class="contact">
      <p class="contact__name">Dale Penwarty</p>
      <p class="contact__role">President</p>
      <ul class="contact__list">
        <li class="contact__item">
          <svg viewBox="0 0 24 24"><path d="M6.6 10.8a15 15 0 0 0 6.6 6.6l2.2-2.2a1 1 0 0 1 1-.25 11.4 11.4 0 0 0 3.6.57 1 1 0 0 1 1 1V20a1 1 0 0 1-1 1A17 17 0 0 1 3 4a1 1 0 0 1 1-1h3.5a1 1 0 0 1 1 1c0 1.25.2 2.45.57 3.57a1 1 0 0 1-.25 1z"/></svg>
          517.608.2391
        </li>
        <li class="contact__item">
          <svg viewBox="0 0 24 24"><path d="M2 5h20v14H2zm2 2v.5l8 5 8-5V7l-8 5z"/></svg>
          hello@merrowsail.com
        </li>
        <li class="contact__item">
          <svg viewBox="0 0 24 24"><circle cx="12" cy="12" r="10"/></svg>
          www.merrowsail.com
        </li>
      </ul>
    </div>
    <div class="rule"></div>
    <p class="address">Your address, city<br>state, ZIP 0000</p>
  </section>

  <section class="card card--back" aria-label="Card back">
    <div class="brand">
      <span class="brand__mark"></span>
      <span class="brand__name">Merrow Sailcraft Works</span>
    </div>
  </section>
</main>
</body>
</html>
```